QBrook718 Business Card Design

I am in need of a business card design.

Business Name: Harbor Stone 718 or Qbrook718 (we can try the business card with both variations)

I would like it to be somewhat different from the "average" business card

What do we do?

We link up with distributors of different items and we Market their products, sell their products, fulfill the shipment, and handle all customer service that goes along with it.

I will be uploading our logo as well as other business card ideas that i have seen and liked on the web.

I like the style of the "graphic design" business card that i uploaded. I was thinking maybe something like that but instead would read.

SYNC | SELL | SHIP

With maybe:
a computer or a Sync icon underneath SYNC
Some form of money sign underneath Sell
a delivery truck or something underneath SHIP.

And then I was thinking maybe put the logo on the back side like in the other business card that i uploaded.

I definitely want a double sided business card.

These are only my suggestions and if i was very confident in my idea then I wouldn't have to be on here. (So make what you think is nice because my opinion is probably not so great anyway!!)

Everything can be changed.

ALSO, For the logo
We can try and remove the text multi channel selling

For the Business card contact info:
Tom Haskins
CEO
2419 Pelkey Avenue
J7R-2B8
Montreal, Quebec

Thanks

Target Market(s)

Businesses

Industry/Entity Type

Information Technology

Font styles to use
Serif
Sans Serif
Decorative

Colors
34a6d6
33b8a4
aaaaaa
85cae6
33a6d7
0492cd
9d9d9d

Requirements
Must have
• Double Sided Business card
Nice to have
• Illustration graphics / Icons underneath the main points

```html
<!DOCTYPE html>
<html lang="en">
<head>
<meta charset="utf-8">
<title>Qbrook718 Business Card</title>
<link href="https://fonts.googleapis.com/css2?family=Open+Sans:wght@400;600;700&display=swap" rel="stylesheet">
<style>
  :root {
    --stage: #151515;
    --card-white: #ffffff;
    --brand-blue: #29a8e0;
    --brand-green: #8dc63f;
    --ink: #333333;
    --line-light: rgba(255,255,255,0.55);
    --white: #ffffff;
  }
  * { margin: 0; padding: 0; box-sizing: border-box; }
  html, body { width: 1200px; height: 900px; overflow: hidden; }
  body {
    background: var(--stage);
    font-family: "Open Sans", Arial, sans-serif;
    position: relative;
  }
  .card {
    position: absolute;
    top: 170px;
    width: 347px;
    height: 561px;
    box-shadow: 0 6px 18px rgba(0,0,0,0.5);
    overflow: hidden;
  }
  .card--front { left: 259px; background: var(--card-white); }
  .card--back { left: 631px; background: var(--brand-blue); }

  .tab {
    position: absolute;
    left: 102px;
    width: 143px;
    height: 30px;
    background: var(--brand-blue);
  }
  .tab--top { top: 0; }
  .tab--bottom { bottom: 0; }

  .brand {
    position: absolute;
    left: 0; right: 0;
    display: flex;
    align-items: center;
    justify-content: center;
    gap: 10px;
    font-weight: 700;
    font-size: 50px;
    letter-spacing: -1px;
  }
  .brand-dot {
    width: 16px; height: 16px;
    border-radius: 50%;
  }
  .card--front .brand { top: 150px; color: var(--brand-blue); }
  .card--front .brand-dot { background: var(--brand-blue); }
  .card--back .brand { top: 275px; color: var(--white); }
  .card--back .brand-dot { background: var(--white); }

  .person {
    position: absolute;
    top: 277px; left: 0; right: 0;
    text-align: center;
  }
  .person-name {
    color: var(--brand-blue);
    font-size: 25px;
    line-height: 32px;
    text-transform: uppercase;
  }
  .person-role {
    color: var(--brand-green);
    font-size: 14px;
    line-height: 20px;
  }

  .contact {
    position: absolute;
    top: 377px; left: 0; right: 0;
    display: flex;
    flex-direction: column;
    align-items: center;
    gap: 2px;
    color: var(--ink);
    font-size: 14px;
    line-height: 19px;
  }
  .contact-item { display: flex; align-items: center; gap: 9px; }
  .contact-item svg { width: 11px; height: 11px; fill: var(--brand-blue); }

  .address {
    position: absolute;
    top: 465px; left: 0; right: 0;
    text-align: center;
    color: var(--ink);
    font-size: 14px;
    line-height: 17px;
  }

  .services-rule {
    position: absolute;
    top: 467px; left: 0; right: 0;
    height: 1px;
    background: var(--line-light);
  }
  .services {
    position: absolute;
    top: 436px; left: 52px;
    display: flex;
    gap: 23px;
  }
  .service {
    width: 64px; height: 64px;
    border-radius: 50%;
    border: 1px solid var(--line-light);
    background: var(--brand-blue);
    display: flex;
    align-items: center;
    justify-content: center;
  }
  .service svg { width: 34px; height: 34px; fill: var(--white); }
  .website {
    position: absolute;
    top: 509px; left: 0; right: 0;
    text-align: center;
    color: var(--white);
    font-size: 14px;
    font-weight: 600;
  }
</style>
</head>
<body>
  <section class="card card--front">
    <div class="tab tab--top"></div>
    <div class="brand"><span class="brand-dot"></span>Qbrook718</div>
    <div class="person">
      <div class="person-name">Tom Haskins</div>
      <div class="person-role">CEO</div>
    </div>
    <div class="contact">
      <div class="contact-item">
        <svg viewBox="0 0 12 12" aria-hidden="true"><path d="M1 3.5C1 2 2.5 1.5 6 1.5S11 2 11 3.5v1H8.5V3.5h-5v1H1zM3 5h6l2 5H1z"/></svg>
        <span>514-555-0172</span>
      </div>
      <div class="contact-item">
        <svg viewBox="0 0 12 12" aria-hidden="true"><path d="M1 2.5h10v7H1z M1.5 3l4.5 3.5L10.5 3" stroke="#fff" stroke-width="0.8"/></svg>
        <span>hello@qbrook718.com</span>
      </div>
    </div>
    <div class="address">
      2419 Pelkey Avenue<br>
      J7R-2B8 Montreal, Quebec
    </div>
    <div class="tab tab--bottom"></div>
  </section>

  <section class="card card--back">
    <div class="brand"><span class="brand-dot"></span>Qbrook718</div>
    <div class="services-rule"></div>
    <div class="services">
      <div class="service" aria-label="Sync">
        <svg viewBox="0 0 34 34" aria-hidden="true">
          <path d="M17 7a10 10 0 0 1 9.4 6.6L29 12l-1 8-7-3.5 2.6-1.5A7 7 0 0 0 10.4 14L7.6 13A10 10 0 0 1 17 7z"/>
          <path d="M17 27a10 10 0 0 1-9.4-6.6L5 22l1-8 7 3.5-2.6 1.5A7 7 0 0 0 23.6 20l2.8 1A10 10 0 0 1 17 27z"/>
        </svg>
      </div>
      <div class="service" aria-label="Sell">
        <svg viewBox="0 0 34 34" aria-hidden="true">
          <text x="17" y="28" text-anchor="middle" font-family="Open Sans, Arial, sans-serif" font-weight="700" font-size="30" fill="#fff">$</text>
        </svg>
      </div>
      <div class="service" aria-label="Ship">
        <svg viewBox="0 0 34 34" aria-hidden="true">
          <path d="M9 10h15l6 6v7H9z"/>
          <path d="M24 11.5h0.5l4.5 4.5H24z" fill="#29a8e0"/>
          <circle cx="13" cy="24" r="3" stroke="#29a8e0" stroke-width="1.2"/>
          <circle cx="25" cy="24" r="3" stroke="#29a8e0" stroke-width="1.2"/>
          <rect x="1" y="13" width="6" height="1.5"/>
          <rect x="2" y="16.5" width="5" height="1.5"/>
          <rect x="3" y="20" width="4" height="1.5"/>
        </svg>
      </div>
    </div>
    <div class="website">www.qbrook718.com</div>
  </section>
</body>
</html>
```